Real Estate Business card design

Company Name: Tamarind Holdings, LLC
subtitle: We pay cash for houses!
Daniel Whitcombe
Managing Director
555-214-0963
Dan@TamarindHoldingsLLC.example
www.TamarindHoldingsLLC.example

We pay referral fees for Seller and Buyer leads.

Back:
We offer referral fees for Seller and Buyer leads that close.

Please contact Hal at 555-214-0963 with your referrals or to learn more about the referral program!

I am open to different color options but I am going for a classic, elegant, clean, and professional look. Please use logo as a reference.

Target Market(s)

People selling their homes and people in the market for buying homes.

Contact Information for Business Card

please see project description

Font styles to use
Serif
Sans Serif
Script

Requirements
Must have
• must have my logo in it
Nice to have
• I like cards that are split down the middle but please come up with a few mock ups. Open to any color scheme.

```html
<!DOCTYPE html>
<html lang="en">
<head>
<meta charset="UTF-8">
<title>Tamarind Holdings, LLC – Business Card</title>
<link rel="stylesheet" href="https://fonts.googleapis.com/css2?family=Montserrat:wght@300;400;500;700&family=Open+Sans:ital,wght@1,600&display=swap">
<style>
  :root {
    --backdrop: #e6e1da;
    --tan: #b58f6e;
    --sand: #d3b383;
    --slate: #444c59;
    --paper: #f1f1f1;
    --white: #ffffff;
  }
  * { margin: 0; padding: 0; box-sizing: border-box; }
  html, body { width: 900px; height: 1200px; overflow: hidden; }
  body {
    position: relative;
    background: var(--backdrop);
    font-family: "Montserrat", sans-serif;
    color: var(--slate);
  }
  .card {
    position: absolute;
    width: 773px;
    height: 444px;
    box-shadow: 0 6px 18px rgba(0,0,0,0.18);
    overflow: hidden;
  }
  /* Front */
  .card-front { left: 72px; top: 136px; background: var(--paper); }
  .name-panel {
    position: absolute; left: 0; top: 0;
    width: 292px; height: 100%;
    background: var(--tan);
  }
  .person-name {
    position: absolute; left: 16px; width: 255px; top: 88px;
    text-align: right; white-space: nowrap;
    letter-spacing: 1px;
  }
  .person-name .first { display: block; font-size: 44px; line-height: 48px; font-weight: 300; color: var(--white); }
  .person-name .last { display: block; font-size: 34px; line-height: 46px; font-weight: 700; color: var(--slate); letter-spacing: 0.5px; }
  .company { position: absolute; left: 328px; top: 92px; }
  .company-name { font-size: 20px; font-weight: 400; color: var(--slate); }
  .company-tagline {
    font-family: "Open Sans", sans-serif;
    font-style: italic; font-weight: 600;
    font-size: 21px; color: var(--tan); margin-top: 4px;
  }
  .contact-list { position: absolute; left: 328px; top: 199px; list-style: none; }
  .contact-list li {
    display: flex; align-items: center; gap: 12px;
    height: 44px; font-size: 19px; color: #222831;
  }
  .contact-list svg { width: 24px; height: 20px; fill: var(--slate); flex: none; }
  .referral-bar {
    position: absolute; left: 43px; top: 374px;
    width: 686px; height: 25px;
    background: var(--slate); color: var(--white);
    font-size: 19px; letter-spacing: 2.6px; line-height: 25px;
    text-align: center; white-space: nowrap;
  }
  /* Back */
  .card-back { left: 74px; top: 628px; height: 440px; background: var(--slate); color: var(--white); }
  .back-headline {
    position: absolute; top: 42px; width: 100%;
    text-align: center; font-size: 18px; letter-spacing: 2.6px; white-space: nowrap;
  }
  .wordmark {
    position: absolute; top: 206px; width: 100%;
    text-align: center; font-weight: 500; color: var(--white);
  }
  .wordmark .main { display: block; font-size: 58px; line-height: 64px; }
  .wordmark .sub { display: block; font-size: 27px; letter-spacing: 2px; line-height: 38px; }
  .contact-band {
    position: absolute; left: 26px; top: 349px;
    width: 719px; height: 65px;
    background: var(--sand); color: var(--slate);
    text-align: center; font-size: 19px; line-height: 26px; padding-top: 7px;
    letter-spacing: 1.6px; white-space: nowrap;
  }
  .contact-band strong { font-weight: 700; }
</style>
</head>
<body>
  <section class="card card-front">
    <div class="name-panel"></div>
    <h1 class="person-name"><span class="first">DANIEL</span><span class="last">WHITCOMBE</span></h1>
    <div class="company">
      <p class="company-name">Tamarind Holdings, LLC</p>
      <p class="company-tagline">We pay cash for houses!</p>
    </div>
    <ul class="contact-list">
      <li><svg viewBox="0 0 24 20"><path d="M2 7c3-4 17-4 20 0l-1 3-4-1V7c-3-1-7-1-10 0v2l-4 1zM6 10h12l3 8H3z"/></svg>555-214-0963</li>
      <li><svg viewBox="0 0 24 20"><path d="M1 2h22v16H1zM3 4v1l9 6 9-6V4zM3 8v8h18V8l-9 6z"/></svg>Dan@TamarindHoldingsLLC.example</li>
      <li><svg viewBox="0 0 24 24"><path d="M12 1a11 11 0 1 0 0 22 11 11 0 0 0 0-22zm0 2c1.5 1.8 2.4 4 2.7 6H9.3C9.6 7 10.5 4.8 12 3zM3.2 11h4.1c.1 2.3.8 4.5 2 6.5A9 9 0 0 1 3.2 11zm0-2a9 9 0 0 1 6.1-6.5C8.1 4.5 7.4 6.7 7.3 9zm6.1 2h5.4c-.2 2.3-1.1 4.6-2.7 6.6-1.6-2-2.5-4.3-2.7-6.6zm5.4 6.5c1.2-2 1.9-4.2 2-6.5h4.1a9 9 0 0 1-6.1 6.5zM16.7 9c-.1-2.3-.8-4.5-2-6.5A9 9 0 0 1 20.8 9z"/></svg>www.TamarindHoldingsLLC.example</li>
    </ul>
    <p class="referral-bar">We pay referral fees for Seller and Buyer leads</p>
  </section>

  <section class="card card-back">
    <p class="back-headline">We offer referral fees for Seller and Buyer leads that close.</p>
    <p class="wordmark"><span class="main">Tamarind</span><span class="sub">Holdings, LLC</span></p>
    <p class="contact-band"><strong>Please contact Hal at 555-214-0963</strong> with your<br>referrals or to learn more about the referral program!</p>
  </section>
</body>
</html>
```